High End Personalized Functional Medicine in Women's Health

We are adding new and exciting personalized medicine services to our Women's Health Care practice focusing on health optimization and anti-aging as well as hormone replacement therapy and need a high end brochure to educate patients about these services. We would like to see a zen-like design that has feminine appeal. Our office colors are vibrant but soothing. We have utilized the concepts of feng shui to optimize our positive energy. The exterior of the building is peach and cream and these colors would blend with that energy The final design should communicate a sense that you can take control of your health and aging.
Updates

Target Market(s)

Females age 35-65 with annual income >$75000/year

Industry/Entity Type

Health And Wellness

Logo Text

Bright Path is the company name. Our sister company is Mesa Rio Ob/Gyn

Font styles to use
Serif

Colors

Designer to choose colors to be used in the design.

Requirements
Must have
• My project must have clean lines. I like a strong feminine appearance, not a fluffy curvy feminine look. Professional appearance, Brochure would be on thicker card stock. A strong front page that makes you want to open the brochure
Nice to have
• Eye catching photos that complement our message . I am not tied to the peach and cream color recommendation, but find those colors feminine but not so cliche as pinks and purples.
Should not have
• frilly design

```html
<!DOCTYPE html>
<html lang="en">
<head>
<meta charset="utf-8">
<title>Bright Path Functional Medicine Brochure</title>
<link href="https://fonts.googleapis.com/css2?family=Oswald:wght@500;600;700&family=Open+Sans:ital,wght@0,400;0,600;0,700;1,400&display=swap" rel="stylesheet">
<style>
  :root{
    --stage:#e4e4e4;
    --ink:#2a2a2a;
    --dark:#262626;
    --peach:#e9b28a;
    --peach-soft:#f6dcc7;
    --cream:#fdf7f1;
    --accent:#e2955f;
    --muted:#555555;
    --white:#ffffff;
  }
  *{box-sizing:border-box;margin:0;padding:0}
  html,body{width:1200px;height:1200px;overflow:hidden}
  body{background:var(--stage);font-family:"Open Sans",Arial,sans-serif;color:var(--ink);position:relative}
  .spread{position:absolute;left:40px;width:1120px;height:540px;display:flex;box-shadow:0 6px 18px rgba(0,0,0,.18)}
  .spread--outside{top:30px}
  .spread--inside{top:630px}
  .page{position:relative;width:560px;height:540px;overflow:hidden;background:var(--white)}
  .heading{font-family:"Oswald",Arial,sans-serif;text-transform:uppercase;font-weight:600;letter-spacing:.3px;line-height:1.1}
  .body-copy{font-size:8.4px;line-height:1.45;color:var(--muted)}
  .photo{position:absolute}
  .brand{font-family:"Oswald",Arial,sans-serif;font-weight:600;letter-spacing:1px;text-transform:uppercase;display:flex;align-items:center;gap:8px}
  .brand__mark{width:14px;height:14px;background:var(--peach)}

  /* back cover */
  .back{background:linear-gradient(180deg,#f3f3f3 0%,#ffffff 40%)}
  .back__panel{position:absolute;left:0;top:50px;width:380px;height:370px;background:linear-gradient(180deg,var(--peach) 0%,var(--peach-soft) 55%,var(--cream) 100%)}
  .back__photo{left:30px;top:75px;width:330px;height:180px;border:5px solid var(--white);box-shadow:0 3px 8px rgba(0,0,0,.2);background:linear-gradient(160deg,#8c9a6a,#6f7d52 55%,#4f5a3a)}
  .back__title{position:absolute;left:30px;top:270px;font-size:20px;color:var(--ink)}
  .back__title small{display:block;font-size:10px}
  .back__text{position:absolute;left:30px;top:318px;width:330px;border-left:2px solid var(--accent);padding-left:8px}
  .back__text p+p{margin-top:6px}
  .back__band{position:absolute;left:0;bottom:0;width:560px;height:120px;background:var(--dark)}
  .back__brand{position:absolute;left:30px;bottom:38px;font-size:30px;color:var(--white)}
  .contact{position:absolute;right:30px;bottom:28px;color:var(--white);font-size:10px;line-height:1.7}
  .contact__row{display:flex;align-items:center;gap:7px}
  .contact__row--phone{font-family:"Oswald",Arial,sans-serif;font-size:20px;font-weight:500}
  .contact svg{flex:none}

  /* front cover */
  .front__top{position:absolute;left:0;top:0;width:560px;height:70px;display:flex;align-items:center;justify-content:center}
  .front__brand{font-size:30px;color:var(--ink)}
  .front__photo{left:0;top:70px;width:560px;height:470px;background:radial-gradient(ellipse at 55% 38%,#c9a27b 0%,#a98457 20%,#6f8f3e 42%,#3f6a26 100%)}
  .front__band{position:absolute;left:0;bottom:0;width:560px;height:150px}
  .front__headline{position:absolute;left:60px;top:402px;font-size:34px;color:var(--ink)}
  .front__subline{position:absolute;left:60px;top:452px;font-size:34px;color:var(--white)}
  .front__url{position:absolute;left:62px;top:508px;color:#cfcfcf;font-size:9px;letter-spacing:1px}

  /* inside left */
  .intro{position:absolute;left:0;top:0;width:560px;height:250px;background:linear-gradient(90deg,var(--peach-soft) 0%,var(--cream) 100%)}
  .intro__bar{position:absolute;left:30px;top:34px;width:50px;height:5px;background:var(--accent)}
  .intro__title{position:absolute;left:30px;top:44px;width:210px;font-size:27px;color:var(--ink);font-weight:700}
  .intro__aim{position:absolute;left:30px;top:118px;width:210px;font-size:12.5px;line-height:1.35;color:var(--ink)}
  .intro__bio{position:absolute;left:262px;top:30px;width:270px;font-size:8.6px;line-height:1.45;color:var(--ink)}
  .reviews{position:absolute;left:30px;top:215px;width:510px;height:88px;background:var(--white);box-shadow:0 2px 8px rgba(0,0,0,.12);display:flex}
  .reviews__head{width:220px;padding:14px 10px 0 14px;font-size:11px;color:var(--ink)}
  .reviews__name{display:inline-block;margin-top:3px;background:var(--peach);padding:1px 6px;color:var(--ink)}
  .reviews__list{flex:1;padding:12px 10px 0 6px;display:flex;flex-direction:column;gap:8px}
  .quote{font-size:8.6px;font-style:italic;color:var(--muted);padding-left:14px;position:relative;line-height:1.4}
  .quote::before{content:"\201C";position:absolute;left:0;top:-4px;font-size:18px;color:var(--accent);font-style:normal;font-family:Georgia,serif}
  .quote b{display:block;font-weight:600;color:var(--ink)}
  .qa-stack{position:absolute;left:30px;top:316px;width:218px;display:flex;flex-direction:column;gap:9px}
  .qa__title{font-size:11px;color:var(--ink);margin-bottom:4px}
  .qa__rule{width:30px;height:2px;background:var(--accent);margin-bottom:4px}
  .qa .body-copy{font-size:8px;line-height:1.38}
  .inside-left__photo{left:258px;top:303px;width:302px;height:237px;background:linear-gradient(170deg,#dfe6e8 0%,#f4f4f2 50%,#c9d3cf 100%)}

  /* inside right */
  .inside-right{background:linear-gradient(90deg,#f1f1f1 0%,#ffffff 60%)}
  .symptoms{position:absolute;left:28px;top:28px;width:290px}
  .symptoms__title{font-size:12px;color:var(--ink)}
  .symptoms__rule{width:30px;height:2px;background:var(--accent);margin:4px 0 10px}
  .symptom{display:flex;gap:10px;margin-bottom:11px}
  .symptom__icon{flex:none;width:22px;height:22px}
  .symptom__name{font-weight:700;font-size:10.5px;color:var(--ink);margin-bottom:2px}
  .column{position:absolute;right:0;top:0;width:222px;height:540px;background:var(--dark)}
  .column__block{position:absolute;left:16px;width:194px;color:#e9e9e9}
  .column__block--first{top:18px}
  .column__block--second{top:330px}
  .column__title{font-size:11.5px;color:var(--white);margin-bottom:5px}
  .column .body-copy{color:#d6d6d6;font-size:8px;line-height:1.35}
  .column__photo{left:0;top:205px;width:222px;height:113px;background:linear-gradient(150deg,#d9d2c8,#a9a39a 50%,#6e6a65)}
</style>
</head>
<body>

<section class="spread spread--outside">
  <article class="page back">
    <div class="back__panel"></div>
    <div class="photo back__photo" role="img" aria-label="Photo of the doctor sitting outdoors with her family"></div>
    <h2 class="back__title heading">Dr. Alvarez<small>with family</small></h2>
    <div class="back__text body-copy">
      <p>Dr. Alvarez lives in the valley with her husband and two children. Weekends find the family hiking mesa trails and cooking together.</p>
      <p>She believes caring for patients starts with caring for yourself, and outside the clinic she teaches yoga and mentors young physicians.</p>
    </div>
    <div class="back__band"></div>
    <div class="back__brand brand"><span class="brand__mark"></span>Bright Path</div>
    <div class="contact">
      <div class="contact__row contact__row--phone">
        <svg width="14" height="14" viewBox="0 0 24 24"><path d="M6.6 10.8a15 15 0 0 0 6.6 6.6l2.2-2.2a1 1 0 0 1 1-.25 11.4 11.4 0 0 0 3.6.57 1 1 0 0 1 1 1V20a1 1 0 0 1-1 1A17 17 0 0 1 3 4a1 1 0 0 1 1-1h3.5a1 1 0 0 1 1 1c0 1.25.2 2.45.57 3.57a1 1 0 0 1-.25 1z" fill="var(--peach)"/></svg>
        (505)555-0142
      </div>
      <div class="contact__row">
        <svg width="12" height="10" viewBox="0 0 24 18"><rect x="1" y="1" width="22" height="16" rx="2" fill="none" stroke="var(--peach)" stroke-width="2"/><path d="M1 2l11 8 11-8" fill="none" stroke="var(--peach)" stroke-width="2"/></svg>
        hello@brightpathhealth.com
      </div>
      <div class="contact__row">
        <svg width="12" height="12" viewBox="0 0 24 24"><circle cx="12" cy="12" r="10" fill="none" stroke="var(--peach)" stroke-width="2"/><path d="M2 12h20M12 2c3 3 3 17 0 20M12 2c-3 3-3 17 0 20" fill="none" stroke="var(--peach)" stroke-width="1.5"/></svg>
        www.brightpathhealth.com
      </div>
    </div>
  </article>

  <article class="page front">
    <header class="front__top">
      <div class="front__brand brand"><span class="brand__mark"></span>Bright Path</div>
    </header>
    <div class="photo front__photo" role="img" aria-label="Photo of a smiling woman in a wide straw sun hat in a green park"></div>
    <svg class="front__band" viewBox="0 0 560 150" preserveAspectRatio="none" aria-hidden="true">
      <polygon points="0,58 560,20 560,150 0,150" fill="var(--dark)"/>
    </svg>
    <h1 class="front__headline heading">Bright Path</h1>
    <p class="front__subline heading">Functional Medicine</p>
    <p class="front__url">www.brightpathhealth.com</p>
  </article>
</section>

<section class="spread spread--inside">
  <article class="page inside-left">
    <div class="intro">
      <div class="intro__bar"></div>
      <h2 class="intro__title heading">Functional Medicine's</h2>
      <p class="intro__aim">aim is to heal the physical body in order to engage in our life purpose of connection and emotional and spiritual growth.</p>
      <p class="intro__bio">Dr. Elena Alvarez specializes in women's health and has over 25 years of experience. She is an expert in bio-identical hormone replacement therapy and has been a Dermavita bio-identical hormone pellet practitioner for over 10 years. Dr. Alvarez has been practicing functional medicine for many years with a primary focus on hormone therapy, medical weight loss, and lifestyle change. She has recently expanded her practice to incorporate additional services including healing with a focus on adrenal, gastrointestinal and detoxification programs. Dr. Alvarez is a practitioner of the Hale Method for functional medicine and works closely with Dr. Marcus Hale as her mentor in the development of individual treatment protocols for our patients. Dr. Hale has over 25 years of experience in functional medicine.</p>
    </div>
    <div class="reviews">
      <h3 class="reviews__head heading">What do patients' have to say about their experience with<br><span class="reviews__name">Dr. Alvarez</span></h3>
      <div class="reviews__list">
        <p class="quote">I finally feel like myself again, rested, focused and full of energy every day.<b>Patient review</b></p>
        <p class="quote">Caring, thorough and truly attentive to every question.<b>Patient review</b></p>
      </div>
    </div>
    <div class="qa-stack">
      <div class="qa">
        <h3 class="qa__title heading">Why should you consider a functional medicine visit?</h3>
        <div class="qa__rule"></div>
        <p class="body-copy">You are tired of feeling tired. You can't even focus on the future because you are so overwhelmed. The pain of being unable to think clearly and being too tired to exercise are your daily reality. Your life goals seem like too much to think about, you just have to get through today.</p>
      </div>
      <div class="qa">
        <h3 class="qa__title heading">Who else should consider a functional medicine visit?</h3>
        <div class="qa__rule"></div>
        <p class="body-copy">You want to achieve OPTIMAL health with a personalized medicine approach. You are eating well, exercising and engaging in stress reducing activities such as meditation. You want to minimize the effects of aging and are ready to take a proactive approach to the highest level of health you can achieve.</p>
      </div>
    </div>
    <div class="photo inside-left__photo" role="img" aria-label="Photo of a female doctor in a white coat holding a card"></div>
  </article>

  <article class="page inside-right">
    <div class="symptoms">
      <h3 class="symptoms__title heading">What symptoms do we treat?</h3>
      <div class="symptoms__rule"></div>

      <div class="symptom">
        <svg class="symptom__icon" viewBox="0 0 24 24" aria-hidden="true"><circle cx="12" cy="12" r="10" fill="none" stroke="var(--accent)" stroke-width="1.6"/><path d="M12 7v5l3 3" fill="none" stroke="var(--accent)" stroke-width="1.6"/></svg>
        <div><p class="symptom__name">Weight gain</p><p class="body-copy">Adrenal dysfunction results in cortisol imbalance. The major function of cortisol is to help balance blood sugar. When cortisol is out of balance, your body will store body fat rather than burning fat for fuel resulting in weight gain. Menopausal hormone imbalance will also result in abdominal weight gain.</p></div>
      </div>
      <div class="symptom">
        <svg class="symptom__icon" viewBox="0 0 24 24" aria-hidden="true"><circle cx="12" cy="12" r="10" fill="none" stroke="var(--accent)" stroke-width="1.6"/><path d="M7 14h10M9 10h.01M15 10h.01" stroke="var(--accent)" stroke-width="1.8" stroke-linecap="round"/></svg>
        <div><p class="symptom__name">Fatigue</p><p class="body-copy">Adrenal exhaustion results from long term stress that depletes cortisol. Testing and correcting cortisol will improve energy levels. Long term stress can result in mitochondrial dysfunction and organic acid tests can tell us how to support your mitochondria.</p></div>
      </div>
      <div class="symptom">
        <svg class="symptom__icon" viewBox="0 0 24 24" aria-hidden="true"><circle cx="12" cy="12" r="10" fill="none" stroke="var(--accent)" stroke-width="1.6"/><path d="M8 16c1-2 7-2 8 0M9 10h.01M15 10h.01" stroke="var(--accent)" stroke-width="1.8" stroke-linecap="round" fill="none"/></svg>
        <div><p class="symptom__name">Depression</p><p class="body-copy">We focus both on cortisol and the brain neurotransmitters dopamine, epinephrine and norepinephrine to evaluate causes of depression. Hormone imbalance can also result in both anxiety and depression.</p></div>
      </div>
      <div class="symptom">
        <svg class="symptom__icon" viewBox="0 0 24 24" aria-hidden="true"><circle cx="6" cy="16" r="3" fill="none" stroke="var(--accent)" stroke-width="1.6"/><circle cx="12" cy="10" r="3" fill="none" stroke="var(--accent)" stroke-width="1.6"/><circle cx="18" cy="5" r="2.5" fill="none" stroke="var(--accent)" stroke-width="1.6"/></svg>
        <div><p class="symptom__name">Female Hormone Imbalance</p><p class="body-copy">Optimizing hormonal balance is our specialty. We focus on optimizing hormone levels with bio-identical hormones, but also know that adrenal treatment protocols can improve symptoms of hot flashes, night sweats, and foggy thinking.</p></div>
      </div>
      <div class="symptom">
        <svg class="symptom__icon" viewBox="0 0 24 24" aria-hidden="true"><circle cx="12" cy="12" r="10" fill="none" stroke="var(--accent)" stroke-width="1.6"/><path d="M8 9c2 0 2 3 4 3s2-3 4-3M8 15c2 0 2-3 4-3s2 3 4 3" fill="none" stroke="var(--accent)" stroke-width="1.5"/></svg>
        <div><p class="symptom__name">GI problems</p><p class="body-copy">The immune cells that line our digestive tract are regulated by cortisol. Cortisol imbalance results in inflammation and "leaky gut" causing digestive symptoms like bloating, heartburn, constipation, or diarrhea. Utilizing a comprehensive program that includes avoiding inflammatory foods and GutScope stool testing allow us to find underlying infections or sources of inflammation and allow us to develop a focused treatment plan.</p></div>
      </div>
    </div>

    <aside class="column">
      <div class="column__block column__block--first">
        <h3 class="column__title heading">What can I expect from my first visit?</h3>
        <p class="body-copy">During your initial consultation, we want to get to know each other and find out your expectations for health. We will explore your health history and symptoms as well as lifestyle factors including diet and sleep. We will discuss your goals and reasons for getting healthy. We know that we must incorporate lifestyle changes including stress reduction, diet and exercise optimization in any program for healing. We will discuss testing recommendations including blood work, hormone evaluation, cortisol, GI, and organic acid tests as well as nutritional and personal coaching options.</p>
      </div>
      <div class="photo column__photo" role="img" aria-label="Photo of a caring woman comforting a distressed patient"></div>
      <div class="column__block column__block--second">
        <h3 class="column__title heading">What are your treatment protocols based on?</h3>
        <p class="body-copy">Treatment protocols are based on making you feel better with a focused wellness program that treats underlying cause. We want to optimize body systems by reducing inflammation, treating insulin resistance, improving catabolic physiology, and reducing oxidative stress. Treatment protocols are a combination of supplement support and hormone balance in addition to lifestyle optimization. Supplement programs tend to be focused and last approximately 6 months. Hormone programs continue for as long as you have symptoms. We will work together to determine what type of treatment program works best for you.</p>
      </div>
    </aside>
  </article>
</section>

</body>
</html>
```